An organic baby/mommy skin care product company needs a web design

We need a web design for an organic baby and mommy skin care product company based in NY/NJ called "Lumo & Pinnet". We have developed a half dozen of all natural, organic baby/mommy skin care products that apply on different part of body. For instance, baby bottom balm/cream/oil to effectively cure/prevent diaper rash etc.

The design is for main/intro page, product page and shipping/packaging page.The theme/template will be uploaded to a CartVeldo 1.4.7.3 enviroment (also looking for alternative solutions).
Updates

Target Market(s)

Young professional parents, educated stay-home moms, caring grandparents.

Industry/Entity Type

Skin Care Product

Requirements
Must have
• Logo on upper left; slideshow pictures (up to 5) on main page;
Nice to have
• Cute background picture (a boy and a girl, etc) font, colors.
Should not have
• Please do not try to list all/most products on the main page. 2 to 3 feature products from each category should be enough.

```html
<!DOCTYPE html>
<html lang="en">
<head>
<meta charset="UTF-8">
<title>Lumo &amp; Pinnet — Organic Baby &amp; Mommy Skin Care</title>
<link href="https://fonts.googleapis.com/css2?family=Arimo:wght@400;700&family=Prata&display=swap" rel="stylesheet">
<style>
:root{
  --header-bg:#f5e1fb;
  --brand:#3276a8;
  --heading:#2a72ad;
  --body-text:#6e6e6e;
  --dark-text:#444;
  --purple:#c99af0;
  --purple-line:#d48cf0;
  --blue:#8fcdf7;
  --blue-btn:#7ec0f0;
  --green:#93ee93;
  --green-btn:#7ee07e;
  --yellow:#f5ee7a;
  --pink:#fd98a8;
  --link:#2a72ad;
}
*{box-sizing:border-box;margin:0;padding:0}
html,body{width:1200px;height:848px;overflow:hidden;background:#fff;font-family:'Arimo',Arial,sans-serif}
.page{position:relative;width:1200px;height:848px}
.header{position:absolute;left:0;top:0;width:1200px;height:112px;background:var(--header-bg)}
.logo{position:absolute;left:162px;top:8px;font-size:74px;line-height:92px;color:var(--brand);font-weight:400;letter-spacing:-2px}
.utility{position:absolute;top:14px;left:736px;display:flex;align-items:center;font-size:11px;color:#555;letter-spacing:.4px}
.utility svg{margin-right:8px}
.utility .sep{margin:0 12px}
.account{margin-left:24px;display:flex;align-items:center}
.nav{position:absolute;left:160px;top:116px;display:flex;gap:3px}
.nav a{display:block;width:116px;height:26px;border-radius:6px;color:#fff;font-weight:700;font-size:19px;text-align:center;line-height:26px;text-decoration:none;text-shadow:0 1px 2px rgba(0,0,0,.35)}
.nav .home{background:var(--purple)}
.nav .product{background:var(--blue)}
.nav .shipping{background:var(--green)}
.nav .about{background:var(--yellow)}
.nav .contact{background:var(--pink)}
.search{position:absolute;left:834px;top:120px;width:206px;height:22px;border:2px solid var(--green);border-radius:5px;font-size:11px;color:#999;padding:2px 8px;display:flex;justify-content:space-between;align-items:center;background:#fff}
.intro{position:absolute;left:160px;top:158px;width:540px}
.intro h1{font-family:'Prata',Georgia,serif;font-weight:400;font-size:26px;line-height:34px;color:var(--heading)}
.intro p{margin-top:6px;font-size:12.5px;line-height:16px;color:var(--body-text)}
.hero{position:absolute;left:125px;top:277px;width:656px;height:386px;background:radial-gradient(ellipse at 50% 45%,#f3d2bd 0%,#f6dfd0 35%,#fbf1eb 60%,#fff 80%)}
.feature{position:absolute;left:834px;width:206px;height:150px;border:2px solid;border-radius:16px;background:#fff}
.feature .title{position:absolute;left:20px;top:14px;font-size:14px;line-height:18px;color:#333;width:110px}
.feature .shot{position:absolute;right:8px;top:30px;width:100px;height:110px;border-radius:10px}
.feature .order{position:absolute;left:-19px;top:99px;width:84px;height:28px;border-radius:8px;color:#fff;font-weight:700;font-size:12px;line-height:28px;text-align:center}
.f1{top:172px;border-color:var(--purple-line)}
.f2{top:341px;border-color:var(--blue)}
.f3{top:510px;border-color:var(--green)}
.f1 .order{background:var(--green-btn)}
.f2 .order{background:var(--purple-line)}
.f3 .order{background:var(--blue-btn)}
.f1 .shot{background:linear-gradient(180deg,#f4f0f4,#b98ac6)}
.f2 .shot{background:linear-gradient(180deg,#e6eef8,#5b7fc9)}
.f3 .shot{background:linear-gradient(180deg,#f5fbe6,#b7e34a)}
.footer{position:absolute;left:160px;top:679px;width:880px;height:150px;border:2px solid var(--blue);border-radius:22px}
.footer .about-text{position:absolute;left:25px;top:21px;width:630px;font-size:12px;line-height:16px;color:var(--dark-text)}
.footer .about-text p+p{margin-top:15px}
.footer .links{position:absolute;left:26px;top:114px;font-size:12px;font-weight:700;color:var(--link)}
.footer .links span{color:#555;font-weight:400;margin:0 6px}
.footer .divider{position:absolute;left:674px;top:17px;width:2px;height:116px;background:var(--green)}
.footer .label{position:absolute;left:686px;font-size:10px;color:#444;letter-spacing:.5px}
.cards{position:absolute;left:686px;top:44px;display:flex;gap:3px}
.cards i{display:block;width:34px;height:22px;border-radius:2px}
.social{position:absolute;left:686px;top:111px;display:flex;gap:3px}
.social i{display:block;width:22px;height:22px;border-radius:50%}
</style>
</head>
<body>
<div class="page">
  <header class="header">
    <div class="logo">Lumo &amp; Pinnet</div>
    <div class="utility">
      <svg width="24" height="20" viewBox="0 0 24 20" aria-hidden="true"><path d="M1 2h4l3 11h12l2-8H7" fill="none" stroke="#555" stroke-width="1.6"/><circle cx="10" cy="17" r="1.6" fill="#555"/><circle cx="18" cy="17" r="1.6" fill="#555"/></svg>
      <span>Shopping Cart</span><span class="sep">|</span><span>(0) Items</span>
      <span class="account">
        <svg width="22" height="22" viewBox="0 0 22 22" aria-hidden="true"><circle cx="11" cy="6" r="5" fill="#555"/><path d="M1 21c0-6 4-8 10-8s10 2 10 8z" fill="#555"/></svg>
        <span style="margin-top:6px">My Account</span>
      </span>
    </div>
  </header>

  <nav class="nav">
    <a class="home" href="#">Home</a>
    <a class="product" href="#">Product</a>
    <a class="shipping" href="#">Shipping</a>
    <a class="about" href="#">About Us</a>
    <a class="contact" href="#">Contact</a>
  </nav>

  <div class="search">
    <span>Search</span>
    <svg width="14" height="14" viewBox="0 0 14 14" aria-hidden="true"><circle cx="6" cy="6" r="4.5" fill="none" stroke="#999" stroke-width="1.4"/><path d="M9.3 9.3L13 13" stroke="#999" stroke-width="1.6"/></svg>
  </div>

  <section class="intro">
    <h1>Sit libris legimus efficiantur id. His feugiat tractatos</h1>
    <p>Usu vide iudicabit ex. Libris voluptua vix in, falli nobis necessitatibus per ut. An sit vidit invidunt definiebas, eum quas tacimates assueverit ex. Ut magna velit iracundia mea, ei reque homero principes duo.</p>
  </section>

  <div class="hero" role="img" aria-label="Slideshow photo of a smiling baby lying on a white blanket"></div>

  <aside>
    <div class="feature f1">
      <div class="title">Mei dicant quodsi apeirian ad</div>
      <div class="shot" role="img" aria-label="Product photo of a lotion bottle on a folded towel with stones"></div>
      <div class="order">ORDER NOW</div>
    </div>
    <div class="feature f2">
      <div class="title">Mei dicant quodsi apeirian ad</div>
      <div class="shot" role="img" aria-label="Product photo of bath bottles, tubes and rolled towels"></div>
      <div class="order">ORDER NOW</div>
    </div>
    <div class="feature f3">
      <div class="title">Mei dicant quodsi apeirian ad</div>
      <div class="shot" role="img" aria-label="Product photo of a green soap pump bottle"></div>
      <div class="order">ORDER NOW</div>
    </div>
  </aside>

  <footer class="footer">
    <div class="about-text">
      <p>Sit libris legimus efficiantur id. His feugiat tractatos ne, corpora forensibus qui ut. No propriae albucius eam. Eius omnium cum in.</p>
      <p>Usu vide iudicabit ex. Libris voluptua vix in, falli nobis necessitatibus per ut. An sit vidit invidunt definiebas, eum quas tacimates assueverit ex. Ut magna velit iracundia mea, ei reque homero principes duo.</p>
    </div>
    <div class="links">Libris<span>|</span>Legimus<span>|</span>Efficiantur<span>|</span>Feugiat<span>|</span>Tractatos<span>|</span>Corpora<span>|</span>Forensibus<span>|</span>Propriae</div>
    <div class="divider"></div>
    <div class="label" style="top:24px">WE ACEEPT</div>
    <div class="cards">
      <i style="background:#1a4f8a"></i><i style="background:#e9eef5;border:1px solid #ccd"></i><i style="background:#2b4f9e"></i><i style="background:#f0f0f0;border:1px solid #ccc"></i><i style="background:#8a3a92"></i>
    </div>
    <div class="label" style="top:95px">FOLLOW US</div>
    <div class="social">
      <i style="background:#3b5998"></i><i style="background:#5bbde6"></i><i style="background:#2a6ea8"></i><i style="background:#e2e2e2"></i><i style="background:#f08a1c"></i>
    </div>
  </footer>
</div>
</body>
</html>
```